Diagram for consulting firm website

My consulting firm, Tamsworth Consulting, www.tamsworthconsulting-example.com.au, requires a visual diagram in the style and colours of our website to promote "Restructuring services." Please see the two attached files for content and guidance.

```html
<!DOCTYPE html>
<html lang="en">
<head>
<meta charset="utf-8">
<title>Types of Corporate Restructuring</title>
<link href="https://fonts.googleapis.com/css2?family=Lexend:wght@300;400;500;600;700&display=swap" rel="stylesheet">
<style>
  :root {
    --orange: #f7931e;
    --blue: #1da9e8;
    --ink: #1f1f1f;
    --label: #2a2a2a;
    --ring-1: #b3f0fb;
    --ring-2: #88e5f8;
    --ring-3: #5ad6f5;
    --ring-4: #2cc6f1;
    --ring-5: #0fb2ea;
    --paper: #ffffff;
    --icon-bg: #f3f3f3;
  }
  html, body {
    margin: 0;
    padding: 0;
    width: 1200px;
    height: 1200px;
    overflow: hidden;
    background: var(--paper);
  }
  .canvas {
    display: block;
    width: 1200px;
    height: 1200px;
    font-family: "Lexend", sans-serif;
  }
  .pill-label { font-size: 20px; font-weight: 400; fill: var(--ink); text-anchor: middle; }
  .hub-title { font-size: 20px; font-weight: 700; text-anchor: middle; }
  .hub-title.orange { fill: var(--orange); }
  .hub-title.dark { fill: var(--ink); }
  .hub-title.blue { fill: var(--blue); }
  .cash-head { font-size: 15px; font-weight: 600; fill: var(--orange); text-anchor: middle; }
  .ring-label { font-size: 9px; font-weight: 400; fill: var(--label); text-anchor: middle; }
  .radial-label { font-size: 10.5px; font-weight: 400; fill: var(--label); text-anchor: middle; }
  .side-label { font-size: 11px; font-weight: 400; fill: var(--label); }
  .loss-label { font-size: 15px; font-weight: 600; fill: #fff; letter-spacing: 0.3px; }
  .scale-label { font-size: 11px; font-weight: 400; fill: var(--label); text-anchor: middle; }
  .radial { stroke: #1e3f66; stroke-width: 1; fill: none; }
</style>
</head>
<body>
<svg class="canvas" viewBox="0 0 1080 1080" xmlns="http://www.w3.org/2000/svg" role="img" aria-label="Types of corporate restructuring and the path from success to insolvency">
  <defs>
    <filter id="soft-shadow" x="-30%" y="-30%" width="160%" height="160%">
      <feDropShadow dx="0" dy="3" stdDeviation="4" flood-color="#000" flood-opacity="0.16"/>
    </filter>
    <marker id="arrow-head" viewBox="0 0 10 10" refX="9" refY="5" markerWidth="7" markerHeight="7" orient="auto-start-reverse">
      <path d="M0,0 L10,5 L0,10 Z" fill="#1e3f66"/>
    </marker>
    <pattern id="ticks-wide" width="16.5" height="22" patternUnits="userSpaceOnUse"><rect x="0" y="0" width="1.3" height="22" fill="var(--blue)"/></pattern>
    <pattern id="ticks-mid" width="8.6" height="22" patternUnits="userSpaceOnUse"><rect x="0" y="0" width="1.3" height="22" fill="var(--blue)"/></pattern>
    <pattern id="ticks-narrow" width="5.6" height="22" patternUnits="userSpaceOnUse"><rect x="0" y="0" width="1.3" height="22" fill="var(--blue)"/></pattern>
    <pattern id="ticks-dense" width="3.7" height="22" patternUnits="userSpaceOnUse"><rect x="0" y="0" width="1.3" height="22" fill="var(--blue)"/></pattern>
    <path id="loss-path" d="M 240 532 A 300 300 0 0 0 840 532"/>
  </defs>

  <!-- Restructuring types hub -->
  <g class="types-hub">
    <path d="M417,163 A128,128 0 0 1 540,72" fill="none" stroke="var(--orange)" stroke-width="8"/>
    <path d="M540,72 A128,128 0 0 1 663,163" fill="none" stroke="var(--blue)" stroke-width="8"/>
    <path d="M417,237 A128,128 0 0 0 540,328" fill="none" stroke="var(--blue)" stroke-width="8"/>
    <path d="M540,328 A128,128 0 0 0 663,237" fill="none" stroke="var(--orange)" stroke-width="8"/>

    <polyline points="368,131 408,131 408,163 419,163" fill="none" stroke="var(--orange)" stroke-width="3"/>
    <circle cx="368" cy="131" r="5" fill="var(--orange)"/>
    <polyline points="368,280 408,280 408,237 419,237" fill="none" stroke="var(--blue)" stroke-width="3"/>
    <circle cx="368" cy="280" r="5" fill="var(--blue)"/>
    <polyline points="712,131 672,131 672,163 661,163" fill="none" stroke="var(--blue)" stroke-width="3"/>
    <circle cx="712" cy="131" r="5" fill="var(--blue)"/>
    <polyline points="712,280 672,280 672,237 661,237" fill="none" stroke="var(--orange)" stroke-width="3"/>
    <circle cx="712" cy="280" r="5" fill="var(--orange)"/>

    <text class="hub-title orange" x="540" y="178">TYPES OF</text>
    <text class="hub-title dark" x="540" y="205">CORPORATE</text>
    <text class="hub-title blue" x="540" y="232">RESTRUCTURING</text>
  </g>

  <!-- Financial restructuring -->
  <g class="type-pill financial">
    <rect x="49" y="87" width="296" height="92" rx="46" fill="#fff" stroke="var(--orange)" stroke-width="2.5"/>
    <path d="M297,74 A58,58 0 0 1 297,190" fill="none" stroke="var(--orange)" stroke-width="7"/>
    <circle cx="297" cy="132" r="40" fill="var(--icon-bg)" filter="url(#soft-shadow)"/>
    <g class="icon" fill="none" stroke="var(--blue)" stroke-width="2" stroke-linecap="round">
      <rect x="283" y="118" width="5" height="12"/>
      <rect x="291" y="112" width="5" height="18"/>
      <polyline points="280,114 290,106 296,110 305,102"/>
      <circle cx="308" cy="127" r="7" stroke="var(--orange)"/>
      <path d="M278,140 h14 l10,-4 q6,-2 8,2 l-14,10 h-18" />
    </g>
    <text class="pill-label" x="161" y="125">Financial</text>
    <text class="pill-label" x="161" y="151">Restructuring</text>
  </g>

  <!-- Organizational restructuring -->
  <g class="type-pill organizational">
    <rect x="49" y="229" width="296" height="92" rx="46" fill="#fff" stroke="var(--blue)" stroke-width="2.5"/>
    <path d="M297,217 A58,58 0 0 1 297,333" fill="none" stroke="var(--blue)" stroke-width="7"/>
    <circle cx="297" cy="275" r="40" fill="var(--icon-bg)" filter="url(#soft-shadow)"/>
    <g class="icon" fill="none" stroke="var(--orange)" stroke-width="2">
      <circle cx="297" cy="260" r="6"/>
      <circle cx="283" cy="285" r="6"/>
      <circle cx="297" cy="285" r="6"/>
      <circle cx="311" cy="285" r="6"/>
      <path d="M297,266 v6 M283,279 v-5 h28 v5 M297,272 v7"/>
    </g>
    <text class="pill-label" x="157" y="268">Organizational</text>
    <text class="pill-label" x="161" y="294">Restructuring</text>
  </g>

  <!-- Operational restructuring -->
  <g class="type-pill operational">
    <rect x="735" y="85" width="296" height="92" rx="46" fill="#fff" stroke="var(--blue)" stroke-width="2.5"/>
    <path d="M783,73 A58,58 0 0 0 783,189" fill="none" stroke="var(--blue)" stroke-width="7"/>
    <circle cx="783" cy="131" r="40" fill="var(--icon-bg)" filter="url(#soft-shadow)"/>
    <g class="icon" fill="none" stroke="var(--orange)" stroke-width="2">
      <circle cx="778" cy="127" r="10" stroke-dasharray="4 2.3" stroke-width="5"/>
      <circle cx="778" cy="127" r="5"/>
      <circle cx="793" cy="142" r="6" stroke-dasharray="3 2" stroke-width="4"/>
    </g>
    <text class="pill-label" x="918" y="125">Operational</text>
    <text class="pill-label" x="918" y="151">Restructuring</text>
  </g>

  <!-- Strategic restructuring -->
  <g class="type-pill strategic">
    <rect x="735" y="235" width="296" height="92" rx="46" fill="#fff" stroke="var(--orange)" stroke-width="2.5"/>
    <path d="M783,223 A58,58 0 0 0 783,339" fill="none" stroke="var(--orange)" stroke-width="7"/>
    <circle cx="783" cy="281" r="40" fill="var(--icon-bg)" filter="url(#soft-shadow)"/>
    <g class="icon" fill="none" stroke="var(--blue)" stroke-width="2">
      <circle cx="786" cy="276" r="12" stroke-dasharray="4 2.5" stroke-width="5"/>
      <circle cx="786" cy="276" r="5"/>
      <path d="M772,296 h10 l-2,-8 q4,-4 0,-8 q-4,-1 -5,3 l1,5 z"/>
    </g>
    <text class="pill-label" x="918" y="275">Strategic</text>
    <text class="pill-label" x="918" y="301">Restructuring</text>
  </g>

  <!-- Cash flow headings -->
  <text class="cash-head" x="382" y="512">CASH FLOW GOOD</text>
  <text class="cash-head" x="693" y="512">CASH FLOW POOR</text>

  <!-- Distress rings -->
  <g class="distress-rings">
    <rect x="250" y="530" width="595" height="3" fill="var(--blue)"/>
    <path d="M250,532 A290,290 0 0 0 830,532 Z" fill="var(--ring-1)"/>
    <path d="M290,532 A250,250 0 0 0 790,532 Z" fill="var(--ring-2)"/>
    <path d="M337,532 A203,203 0 0 0 743,532 Z" fill="var(--ring-3)"/>
    <path d="M385,532 A155,155 0 0 0 695,532 Z" fill="var(--ring-4)"/>
    <path d="M430,532 A110,110 0 0 0 650,532 Z" fill="var(--ring-5)"/>
  </g>

  <!-- Loss of control arc -->
  <g class="control-arc">
    <path d="M240,532 A300,300 0 0 0 830,586" fill="none" stroke="var(--orange)" stroke-width="22"/>
    <polygon points="852,530 808,582 868,592" fill="var(--orange)"/>
    <text class="loss-label" dy="5"><textPath href="#loss-path" startOffset="50%" text-anchor="middle">LOSS OF MANAGEMENT CONTROL</textPath></text>
  </g>

  <!-- Radial arrows -->
  <line class="radial" x1="543" y1="532" x2="265" y2="598" marker-end="url(#arrow-head)"/>
  <line class="radial" x1="543" y1="532" x2="385" y2="768" marker-end="url(#arrow-head)"/>
  <line class="radial" x1="543" y1="532" x2="705" y2="768" marker-end="url(#arrow-head)"/>
  <line class="radial" x1="543" y1="532" x2="820" y2="598" marker-end="url(#arrow-head)"/>

  <!-- Ring labels -->
  <text class="ring-label" x="543" y="600">Covenant</text>
  <text class="ring-label" x="543" y="612">Breaches</text>
  <text class="ring-label" x="543" y="650">Creditor Pressure</text>
  <text class="ring-label" x="543" y="697">Expensive Refinancing</text>
  <text class="ring-label" x="543" y="744">Equality Value Negligible</text>
  <text class="ring-label" x="532" y="791" transform="rotate(4 532 788)">Creditors In Control Of Strategy</text>

  <!-- Radial labels -->
  <g transform="translate(335,553) rotate(-14)">
    <text class="radial-label" y="0">Underperforming</text>
    <text class="radial-label" y="13">Business</text>
  </g>
  <text class="radial-label" transform="translate(448,597) rotate(57)">Profit Warning</text>
  <text class="radial-label" transform="translate(410,617) rotate(57)">Credit Rating Downgrade</text>
  <text class="radial-label" transform="translate(373,651) rotate(57)">Potential Covenant Breach</text>
  <text class="radial-label" transform="translate(333,668) rotate(57)">Board Still In Control Of Strategy</text>
  <g transform="translate(747,558) rotate(13)">
    <text class="radial-label" y="0">Insolvent</text>
    <text class="radial-label" y="13">Business</text>
  </g>

  <!-- Side labels -->
  <text class="side-label" x="182" y="703" text-anchor="middle">Distressed Operational</text>
  <text class="side-label" x="182" y="718" text-anchor="middle">Restructuring</text>
  <text class="side-label" x="835" y="703">Formal Insolvency</text>
  <text class="side-label" x="835" y="718">Appointment</text>
  <text class="side-label" x="543" y="872" text-anchor="middle">Creditor Advisory / Distressed</text>
  <text class="side-label" x="543" y="887" text-anchor="middle">Corporate Advisory (Financial)</text>

  <!-- Stage scale -->
  <g class="stage-scale">
    <text class="scale-label" x="267" y="957">Success</text>
    <text class="scale-label" x="444" y="957">Stressed</text>
    <text class="scale-label" x="628" y="957">Distressed</text>
    <text class="scale-label" x="813" y="957">Insolvent</text>
    <rect x="185" y="978" width="170" height="20" fill="url(#ticks-wide)"/>
    <rect x="364" y="978" width="172" height="20" fill="url(#ticks-mid)"/>
    <rect x="545" y="978" width="174" height="20" fill="url(#ticks-narrow)"/>
    <rect x="727" y="978" width="171" height="20" fill="url(#ticks-dense)"/>
    <rect x="357" y="962" width="2" height="36" fill="var(--orange)"/>
    <rect x="539" y="962" width="2" height="36" fill="var(--orange)"/>
    <rect x="721" y="962" width="2" height="36" fill="var(--orange)"/>
  </g>
</svg>
</body>
</html>
```